Buch-/E-Book-Cover für Self-Publisher gesucht
Zielgruppe
Ich bin Schriftsteller und möchte neben den Büchern, die bei Verlagen erscheinen, künftig auch eigene Bücher als Selfpublisher veröffentlichen. Dementsprechend ist die Zielgruppe relativ breit gefasst: Leser.
Aufgabenstellung
Da der Markt für Selfpublisher-Bücher groß ist, sollte das Cover einerseits positiv auffallen und andererseits unbedingt so professionell aussehen, dass es im Vergleich zu Verlags-Büchern nicht negativ auffällt.

```html
<!DOCTYPE html>
<html lang="de">
<head>
<meta charset="utf-8">
<title>Hartel Tage – Buchcover</title>
<link rel="stylesheet" href="https://fonts.googleapis.com/css2?family=Roboto+Condensed:wght@700&family=Roboto:wght@300&display=swap">
<style>
  :root {
    --page: #ffffff;
    --ink: #000000;
    --frame: #1a1a1a;
    --curtain-light: #f0262a;
    --curtain-mid: #c9060c;
    --curtain-dark: #5a0003;
  }
  html, body {
    margin: 0;
    padding: 0;
    width: 848px;
    height: 1200px;
    overflow: hidden;
    background: var(--page);
  }
  .canvas {
    display: block;
    width: 848px;
    height: 1200px;
  }
  .cover-frame {
    fill: var(--page);
    stroke: var(--frame);
    stroke-width: 1;
  }
  .title {
    font-family: "Roboto Condensed", "Arial Narrow", sans-serif;
    font-weight: 700;
    fill: var(--ink);
  }
  .title-line-1 { font-size: 120px; }
  .title-line-2 { font-size: 170px; }
  .genre {
    font-family: "Roboto", Arial, sans-serif;
    font-weight: 300;
    font-size: 21px;
    fill: var(--ink);
  }
  .author {
    font-family: "Roboto Condensed", "Arial Narrow", sans-serif;
    font-weight: 700;
    font-size: 31px;
    fill: var(--ink);
  }
</style>
</head>
<body>
<svg class="canvas" viewBox="0 0 848 1200" xmlns="http://www.w3.org/2000/svg">
  <defs>
    <linearGradient id="curtainFill" x1="0" y1="0" x2="1" y2="0.6">
      <stop offset="0" stop-color="var(--curtain-light)"/>
      <stop offset="0.35" stop-color="var(--curtain-mid)"/>
      <stop offset="0.55" stop-color="var(--curtain-dark)"/>
      <stop offset="0.75" stop-color="var(--curtain-light)"/>
      <stop offset="1" stop-color="var(--curtain-mid)"/>
    </linearGradient>
  </defs>

  <rect class="cover-frame" x="97.5" y="137.5" width="606" height="889"/>

  <g class="curtain" transform="translate(98 138)" role="img" aria-label="Roter Bühnenvorhang, den eine Hand zur Seite zieht">
    <path d="M0,0 H605 V451 C560,380 470,300 380,250 C250,180 100,110 0,31 Z" fill="url(#curtainFill)"/>
  </g>

  <text class="title title-line-1" x="232" y="667" textLength="332" lengthAdjust="spacingAndGlyphs">HARTEL</text>
  <text class="title title-line-2" x="232" y="804" textLength="330" lengthAdjust="spacingAndGlyphs">TAGE</text>
  <text class="genre" x="244" y="843" textLength="318" lengthAdjust="spacing">UNTERHALTUNGSROMAN</text>

  <text class="author" x="400" y="994" text-anchor="middle">TALVIN MUREK</text>
</svg>
</body>
</html>
```